Searchable website that will contain information about sites for Bright Harbor Roster.

Once a search is performed the website will show the following information per site:
Title, Description, Screenshot of the site. I'm thinking three items per row.

Number of Pages Required

1 page

Font styles to use
Sans Serif

Colors
ffffff
3176b5

```html
<!DOCTYPE html>
<html lang="en">
<head>
<meta charset="utf-8">
<title>Bright Harbor Roster – Search for a List</title>
<link href="https://fonts.googleapis.com/css2?family=Roboto:wght@300;400;500;700;900&display=swap" rel="stylesheet">
<style>
  :root{
    --white:#ffffff;
    --brand:#3176b5;
    --brand-bright:#3a8fd8;
    --ink-blue:#1f5f9e;
    --hero-bg:#edf6fe;
    --hero-line:#d8e9f8;
    --card-border:#e3e7ec;
    --card-foot:#f6f8fa;
    --shot:#bcbdbf;
    --text-grey:#5d6470;
    --text-dark:#3a3f47;
    --ring:#3aa0e2;
    --fb:#3b5a9a;
    --tw:#4fc0ee;
    --gp:#e85a55;
  }
  *{box-sizing:border-box;margin:0;padding:0}
  html,body{width:1200px;height:1200px;overflow:hidden;background:var(--white);font-family:'Roboto',sans-serif}
  .page{position:relative;width:1200px;height:1200px}
  .abs{position:absolute}

  .brand{display:flex;align-items:center;gap:10px;color:var(--brand-bright);font-weight:300}
  .brand-dot{width:26px;height:26px;border-radius:50%;background:var(--brand)}
  .header-brand{left:264px;top:18px;font-size:20px}

  .nav{position:absolute;left:678px;top:27px;height:13px;display:flex;gap:17px;font-size:9.5px;line-height:13px;color:var(--brand);font-weight:500}
  .nav a{white-space:nowrap;color:inherit;text-decoration:none}
  .contacts-btn{left:881px;top:21px;width:61px;height:23px;border:1px solid #c9def1;background:#f4f9fe;border-radius:2px;font-size:9.5px;font-weight:500;color:var(--brand);display:flex;align-items:center;justify-content:center}

  .hero{left:166px;top:68px;width:866px;height:247px;background:var(--hero-bg);border:1px solid var(--hero-line)}
  .hero-title{left:0;width:1200px;top:110px;text-align:center;font-size:37px;font-weight:700;color:var(--brand)}
  .hero-desc{left:0;width:1200px;top:173px;text-align:center;font-size:13.5px;line-height:19px;font-weight:300;color:var(--brand-bright)}
  .search{left:374px;top:231px;width:452px;height:38px;border:2px solid #cfe4f6;background:var(--white);border-radius:20px;display:flex;align-items:center;justify-content:space-between;padding:0 16px 0 19px;font-size:11px;color:var(--brand)}
  .globe{left:573px;top:294px}

  .card{width:216px;height:272px;background:var(--white);border:1px solid var(--card-border);box-shadow:0 1px 4px rgba(0,0,0,.12);display:flex;flex-direction:column}
  .card-head{height:48px;display:flex;align-items:center;padding:0 12px 0 13px;font-size:11px;color:var(--text-dark)}
  .ring{width:15px;height:15px;border-radius:50%;border:3px solid var(--ring);margin-right:7px}
  .card-head .title{flex:1}
  .card-shot{height:138px;background:var(--shot)}
  .card-desc{height:49px;display:flex;align-items:center;justify-content:center;font-size:8px;color:var(--text-grey)}
  .card-foot{flex:1;background:var(--card-foot);display:flex;align-items:center;justify-content:center;gap:22px;font-size:8px;color:var(--text-grey)}

  .pager{left:258px;top:987px;height:20px;display:flex;border:1px solid #e1e4e8;border-radius:2px;background:#f2f4f6;font-size:6.5px;color:var(--text-dark)}
  .pager span{width:26px;display:flex;align-items:center;justify-content:center;border-right:1px solid #dfe2e6}
  .pager span:first-child{color:#b0b5bc}
  .pager span:last-child{border-right:none;width:21px}

  .footer{left:170px;top:1032px;width:866px;height:168px;background:var(--hero-bg)}
  .footer-brand{left:261px;top:1104px;font-size:12.5px}
  .footer-brand .brand-dot{width:22px;height:22px}
  .fcol{top:1066px;font-size:7.5px;color:var(--ink-blue);font-weight:500}
  .fcol h4{font-size:9px;font-weight:700;margin-bottom:21px}
  .fcol li{list-style:none;height:15.7px}
  .social{display:flex;gap:11px}
  .social span{width:30px;height:30px;border-radius:50%}
  .copy{left:789px;top:1143px;font-size:9px;color:#64a6dd}
</style>
</head>
<body>
<div class="page">
  <div class="abs brand header-brand"><span class="brand-dot"></span>Bright Harbor Roster</div>
  <nav class="nav">
    <a>Home</a><a>About</a><a>Community</a><a>Blog</a>
  </nav>
  <div class="abs contacts-btn">Contacts</div>

  <section class="abs hero"></section>
  <h1 class="abs hero-title">Search for a List</h1>
  <p class="abs hero-desc">A little description about website<br>and how the search works</p>
  <div class="abs search">
    <span>Search Here . . .</span>
    <svg width="18" height="18" viewBox="0 0 18 18" fill="none" stroke="#3a8fd8" stroke-width="2.4"><circle cx="7.5" cy="7.5" r="5.5"/><path d="M11.5 11.5l5 5" stroke-linecap="round"/></svg>
  </div>
  <svg class="abs globe" width="48" height="48" viewBox="0 0 48 48" fill="none" stroke="#7bb8e6" stroke-width="2">
    <circle cx="20" cy="20" r="17"/><path d="M3 20h34M20 3c-7 9-7 25 0 34M20 3c7 9 7 25 0 34"/>
    <circle cx="31" cy="30" r="8" fill="#fff"/><path d="M37 36l7 7" stroke-linecap="round"/>
  </svg>

  <main>
    <article class="abs card" style="left:257px;top:386px">
      <div class="card-head"><span class="ring"></span><span class="title">Site Title</span><svg width="11" height="11" viewBox="0 0 11 11"><rect width="11" height="11" rx="1" fill="#7a7f86"/><path d="M3 8l5-5M4.5 3H8v3.5" stroke="#fff" stroke-width="1.3" fill="none"/></svg></div>
      <div class="card-shot" role="img" aria-label="Screenshot of the site"></div>
      <div class="card-desc">Site Description Goes Here</div>
      <div class="card-foot"><span>Category name &amp; icon</span><span>|</span><span>125&nbsp; clicks</span></div>
    </article>
    <article class="abs card" style="left:492px;top:386px">
      <div class="card-head"><span class="ring"></span><span class="title">Site Title</span><svg width="11" height="11" viewBox="0 0 11 11"><rect width="11" height="11" rx="1" fill="#7a7f86"/><path d="M3 8l5-5M4.5 3H8v3.5" stroke="#fff" stroke-width="1.3" fill="none"/></svg></div>
      <div class="card-shot" role="img" aria-label="Screenshot of the site"></div>
      <div class="card-desc">Site Description Goes Here</div>
      <div class="card-foot"><span>Category name &amp; icon</span><span>|</span><span>125&nbsp; clicks</span></div>
    </article>
    <article class="abs card" style="left:726px;top:386px">
      <div class="card-head"><span class="ring"></span><span class="title">Site Title</span><svg width="11" height="11" viewBox="0 0 11 11"><rect width="11" height="11" rx="1" fill="#7a7f86"/><path d="M3 8l5-5M4.5 3H8v3.5" stroke="#fff" stroke-width="1.3" fill="none"/></svg></div>
      <div class="card-shot" role="img" aria-label="Screenshot of the site"></div>
      <div class="card-desc">Site Description Goes Here</div>
      <div class="card-foot"><span>Category name &amp; icon</span><span>|</span><span>125&nbsp; clicks</span></div>
    </article>
    <article class="abs card" style="left:257px;top:688px">
      <div class="card-head"><span class="ring"></span><span class="title">Site Title</span><svg width="11" height="11" viewBox="0 0 11 11"><rect width="11" height="11" rx="1" fill="#7a7f86"/><path d="M3 8l5-5M4.5 3H8v3.5" stroke="#fff" stroke-width="1.3" fill="none"/></svg></div>
      <div class="card-shot" role="img" aria-label="Screenshot of the site"></div>
      <div class="card-desc">Site Description Goes Here</div>
      <div class="card-foot"><span>Category name &amp; icon</span><span>|</span><span>125&nbsp; clicks</span></div>
    </article>
    <article class="abs card" style="left:492px;top:688px">
      <div class="card-head"><span class="ring"></span><span class="title">Site Title</span><svg width="11" height="11" viewBox="0 0 11 11"><rect width="11" height="11" rx="1" fill="#7a7f86"/><path d="M3 8l5-5M4.5 3H8v3.5" stroke="#fff" stroke-width="1.3" fill="none"/></svg></div>
      <div class="card-shot" role="img" aria-label="Screenshot of the site"></div>
      <div class="card-desc">Site Description Goes Here</div>
      <div class="card-foot"><span>Category name &amp; icon</span><span>|</span><span>125&nbsp; clicks</span></div>
    </article>
    <article class="abs card" style="left:726px;top:688px">
      <div class="card-head"><span class="ring"></span><span class="title">Site Title</span><svg width="11" height="11" viewBox="0 0 11 11"><rect width="11" height="11" rx="1" fill="#7a7f86"/><path d="M3 8l5-5M4.5 3H8v3.5" stroke="#fff" stroke-width="1.3" fill="none"/></svg></div>
      <div class="card-shot" role="img" aria-label="Screenshot of the site"></div>
      <div class="card-desc">Site Description Goes Here</div>
      <div class="card-foot"><span>Category name &amp; icon</span><span>|</span><span>125&nbsp; clicks</span></div>
    </article>
  </main>

  <div class="abs pager"><span>1</span><span>2</span><span>3</span><span>4</span><span>5</span><span>&#9656;</span></div>

  <footer class="abs footer"></footer>
  <div class="abs brand footer-brand"><span class="brand-dot"></span>Bright Harbor Roster</div>
  <div class="abs fcol" style="left:437px"><h4>Quick Links</h4><ul><li>Home</li><li>About</li><li>Community</li><li>Blog</li></ul></div>
  <div class="abs fcol" style="left:555px"><h4>Latest Searches</h4><ul><li>Online Business</li><li>Busines Forums</li><li>Production</li><li>English Partners</li></ul></div>
  <div class="abs fcol" style="left:673px"><h4>About Us</h4><ul><li>About Team</li><li>Our Goals</li><li>Community</li><li>Contact Us</li></ul></div>
  <div class="abs fcol" style="left:789px"><h4 style="margin-bottom:13px">Connect via Social media</h4>
    <div class="social"><span style="background:var(--fb)" role="img" aria-label="Social link 1"></span><span style="background:var(--tw)" role="img" aria-label="Social link 2"></span><span style="background:var(--gp)" role="img" aria-label="Social link 3"></span></div>
  </div>
  <p class="abs copy">© 2018 Lumen Studio Copyrights</p>
</div>
</body>
</html>
```